Business Card for Multi-Brand Sportswear Company

We are looking for a business card which represents our company and the multiple brands within it.

The company: Kelt Athletic (LTD)
The brands: Kelt, PawaLuni, VerdantFlex, Grit and Gale

Employees using these cards would be representing Kelt Athletic, rather than any of the individual brands. You will see a current design within the uploaded files, to give some inspiration. The actual text of the brands is not necessary, but the logos should be on there is some format.

Our creative minds on this are stretched, so we are looking for someone to make this their own, and show us what a good business card should look like.

We may like to get these printed with spot gloss, so keep that in mind with your designs.

www.keltathletic.co.uk

Industry/Entity Type

Business

Contact Information for Business Card

Tom Hollingsworth-Pryce
Operations Manager
(+44) 1632 960 418
Tom@keltathletic.co.uk
www.keltathletic.co.uk

Font styles to use
Sans Serif
Other font styles liked:
• Eurostile

Colors
ffffff

Requirements
Nice to have
• Dark (black) background

```html
<!DOCTYPE html>
<html lang="en">
<head>
<meta charset="utf-8">
<title>Kelt Athletic — Business Card</title>
<link href="https://fonts.googleapis.com/css2?family=Saira:wght@400;500;600&display=swap" rel="stylesheet">
<style>
  :root {
    --stage: #8a8a8a;
    --card: #1f1f1f;
    --card-tone: #2a2a2a;
    --white: #ffffff;
    --accent-red: #d9262c;
    --accent-plum: #5a4a62;
    --muted: #b8b8b8;
  }
  * { box-sizing: border-box; margin: 0; padding: 0; }
  html, body {
    width: 1200px; height: 854px; overflow: hidden;
    background: var(--stage);
    font-family: "Saira", "Helvetica Neue", Arial, sans-serif;
    color: var(--white);
  }
  .card {
    position: absolute; top: 281px;
    width: 512px; height: 293px;
    background: var(--card);
    overflow: hidden;
    box-shadow: 0 6px 18px rgba(0,0,0,0.35);
  }
  .card--front { left: 88px; }
  .card--back { left: 619px; }
  .card__pattern {
    position: absolute; inset: 0;
    background: linear-gradient(125deg, var(--card) 0%, var(--card-tone) 45%, var(--card) 70%, var(--card-tone) 100%);
  }
  .wordmark {
    position: absolute; display: flex; align-items: center; gap: 8px;
    font-weight: 600; color: var(--white); white-space: nowrap; letter-spacing: 0.5px;
  }
  .wordmark__dot { border-radius: 50%; background: var(--accent-red); flex: none; }
  .card--front .wordmark { left: 24px; top: 113px; font-size: 30px; }
  .card--front .wordmark__dot { width: 12px; height: 12px; }
  .card--back .wordmark { left: 50%; transform: translateX(-50%); top: 110px; font-size: 56px; }
  .card--back .wordmark__dot { width: 20px; height: 20px; }

  .brands {
    position: absolute; display: flex; align-items: center;
    font-weight: 500; color: var(--white); white-space: nowrap;
  }
  .brand { display: flex; align-items: center; gap: 4px; }
  .brand__mark { flex: none; }
  .brand__mark--square { background: var(--accent-plum); }
  .brand__mark--red { background: var(--accent-red); }
  .brand__mark--circle { border: 1.5px solid var(--muted); border-radius: 50%; }
  .card--front .brands { left: 68px; top: 186px; gap: 10px; font-size: 8px; }
  .card--front .brand__mark { width: 9px; height: 9px; }
  .card--back .brands { left: 50%; transform: translateX(-50%); top: 232px; gap: 18px; font-size: 15px; }
  .card--back .brand__mark { width: 18px; height: 18px; }

  .contact-name {
    position: absolute; right: 28px; top: 114px;
    font-size: 17px; font-weight: 500; text-align: right; white-space: nowrap;
  }
  .contact-role {
    position: absolute; right: 28px; top: 143px;
    font-size: 14px; font-weight: 400; text-align: right;
  }
  .contact-list {
    position: absolute; left: 312px; top: 195px; list-style: none;
    font-size: 13px; font-weight: 400;
  }
  .contact-list li { display: flex; align-items: center; gap: 9px; height: 24px; white-space: nowrap; }
  .contact-list svg { width: 12px; height: 12px; flex: none; }
</style>
</head>
<body>

<section class="card card--front" aria-label="Business card front">
  <div class="card__pattern" role="img" aria-label="Faint repeated brand pattern across the card"></div>

  <div class="wordmark"><span>Kelt Athletic</span><span class="wordmark__dot"></span></div>

  <div class="brands">
    <span class="brand"><span class="brand__mark brand__mark--square"></span>PawaLuni</span>
    <span class="brand"><span class="brand__mark brand__mark--red"></span>Grit and Gale</span>
    <span class="brand">Kelt</span>
    <span class="brand"><span class="brand__mark brand__mark--circle"></span>VerdantFlex</span>
  </div>

  <h1 class="contact-name">Tom Hollingsworth-Pryce</h1>
  <p class="contact-role">Operations Manager</p>

  <ul class="contact-list">
    <li>
      <svg viewBox="0 0 24 24" fill="none" stroke="currentColor" stroke-width="2"><path d="M5 3h4l2 5-3 2a12 12 0 0 0 6 6l2-3 5 2v4a2 2 0 0 1-2 2A18 18 0 0 1 3 5a2 2 0 0 1 2-2z"/></svg>
      (+44) 1632 960 418
    </li>
    <li>
      <svg viewBox="0 0 24 24" fill="none" stroke="currentColor" stroke-width="2"><rect x="3" y="5" width="18" height="14" rx="1"/><path d="M3 6l9 7 9-7"/></svg>
      Tom@keltathletic.co.uk
    </li>
    <li>
      <svg viewBox="0 0 24 24" fill="none" stroke="currentColor" stroke-width="2"><circle cx="12" cy="12" r="9"/><path d="M3 12h18M12 3a14 14 0 0 1 0 18M12 3a14 14 0 0 0 0 18"/></svg>
      www.keltathletic.co.uk
    </li>
  </ul>
</section>

<section class="card card--back" aria-label="Business card back">
  <div class="card__pattern" role="img" aria-label="Faint repeated brand pattern across the card"></div>

  <div class="wordmark"><span>Kelt Athletic</span><span class="wordmark__dot"></span></div>

  <div class="brands">
    <span class="brand"><span class="brand__mark brand__mark--square"></span>PawaLuni</span>
    <span class="brand"><span class="brand__mark brand__mark--red"></span>Grit and Gale</span>
    <span class="brand">Kelt</span>
    <span class="brand"><span class="brand__mark brand__mark--circle"></span>VerdantFlex</span>
  </div>
</section>

</body>
</html>
```